SOS! The Thistle cafe is in need of a menu face lift!

We need a standout looking menu for our evolving cafe. Our business has grown greatly from our fresh and changing menu, however the menu (look) itself isn't inspiring and is basic.
I have attached some photos of the business and menus I like the look of.
I am open to other ideas (this is why I need your creative help)
Our menu is currently on an A5 clip board, however we are willing to change it a different size if needed.

Would love to have it a multi function eg, used as a takeaway menu as well, possibly bi-fold? Added Wednesday, June 8, 2016

• It would be cool to have some old sea/ pirate references?

```html
<!DOCTYPE html>
<html lang="en">
<head>
<meta charset="utf-8">
<title>The Thistle — Breakfast Menu</title>
<link href="https://fonts.googleapis.com/css2?family=Almendra+SC&family=Macondo&display=swap" rel="stylesheet">
<style>
  :root {
    --backdrop: #2e2419;
    --backdrop-light: #4a3a28;
    --parchment: #f4ecc8;
    --parchment-edge: #d9c48e;
    --ink: #2a1d12;
    --frame-dark: #1c1710;
    --frame-light: #e9dca8;
    --grid: rgba(120, 100, 60, 0.28);
    --banner: #d8c48f;
  }
  * { margin: 0; padding: 0; box-sizing: border-box; }
  html, body { width: 848px; height: 1200px; overflow: hidden; background: var(--backdrop); }
  .menu {
    position: relative;
    width: 848px;
    height: 1200px;
    overflow: hidden;
    font-family: "Macondo", cursive;
    color: var(--ink);
  }
  .backdrop-pattern {
    position: absolute; inset: 0;
    background: radial-gradient(circle at 50% 50%, var(--backdrop-light), var(--backdrop) 75%);
  }
  .parchment {
    position: absolute;
    left: 48px; top: 44px; width: 744px; height: 1080px;
    background: radial-gradient(ellipse at 50% 45%, #fffbe4 0%, var(--parchment) 45%, var(--parchment-edge) 100%);
  }
  .frame { position: absolute; left: 0; top: 0; }
  .skull-art {
    position: absolute; left: 600px; top: 22px; width: 182px; height: 208px;
    background: radial-gradient(circle at 50% 50%, #cdb77c, #7a6236 70%, rgba(60,45,30,0) 72%);
  }
  .compass-art {
    position: absolute; left: 500px; top: 820px; width: 270px; height: 270px;
    border-radius: 50%;
    background: radial-gradient(circle, rgba(150,130,90,0.35), rgba(150,130,90,0) 70%);
  }
  .title-banner {
    position: absolute; left: 136px; top: 106px; width: 428px; height: 72px;
    background: linear-gradient(180deg, #e8d8a6, var(--banner));
    border-radius: 4px;
  }
  .title {
    position: absolute; left: 176px; top: 122px;
    font-family: "Almendra SC", serif;
    font-size: 34px; letter-spacing: 0.5px; color: var(--ink);
    white-space: nowrap;
  }
  .title small { font-size: 19px; }
  .menu-list {
    position: absolute; left: 134px; top: 221px; width: 568px;
    list-style: none;
    font-size: 15.4px;
  }
  .menu-list li {
    height: 21.39px; line-height: 21.39px;
    display: flex; justify-content: space-between;
    white-space: nowrap;
  }
  .dish { font-weight: 700; text-transform: uppercase; }
  .price { font-weight: 700; }
</style>
</head>
<body>
<main class="menu">
  <div class="backdrop-pattern" role="img" aria-label="Dark brown nautical pattern of anchors, ship wheels, compasses and skulls"></div>
  <div class="parchment" role="img" aria-label="Aged parchment sheet with torn edges"></div>

  <svg class="frame" width="848" height="1200" viewBox="0 0 848 1200" aria-hidden="true">
    <g stroke="var(--grid)" stroke-width="1">
      <line x1="136" y1="70" x2="136" y2="1100"/>
      <line x1="332" y1="70" x2="332" y2="1100"/>
      <line x1="544" y1="70" x2="544" y2="1100"/>
      <line x1="80" y1="414" x2="768" y2="414"/>
      <line x1="80" y1="590" x2="768" y2="590"/>
      <line x1="80" y1="765" x2="768" y2="765"/>
      <line x1="80" y1="940" x2="768" y2="940"/>
    </g>
    <rect x="76" y="64" width="694" height="1042" fill="none" stroke="var(--frame-dark)" stroke-width="10"/>
    <rect x="76" y="64" width="694" height="1042" fill="none" stroke="var(--frame-light)" stroke-width="5" stroke-dasharray="22 12"/>
  </svg>

  <div class="compass-art" role="img" aria-label="Faint compass rose"></div>
  <div class="skull-art" role="img" aria-label="Pirate skull with tricorn hat and crossed bones"></div>
  <div class="title-banner" role="img" aria-label="Scroll ribbon banner"></div>
  <h1 class="title">BREAKFAST MENU <small>ALL DAY</small></h1>

  <ul class="menu-list">
    <li><span class="dish">Toast – served buttered</span></li>
    <li><span><span class="dish">2 Slices</span> - sourdough white or wholemeal,</span></li>
    <li><span>block white or wholemeal, or turkish</span><span class="price">$4.5</span></li>
    <li><span>jam, savoury spread, honey, peanut butter</span></li>
    <li><span>or cinnamon sugar</span><span class="price">+$0.5</span></li>
    <li><span class="dish">GF Bread (2)</span><span class="price">$5.5</span></li>
    <li><span><span class="dish">Turkish Raisin (2)</span> toast</span><span class="price">$5.5</span></li>
    <li><span class="dish">Banana Bread (GF)</span><span class="price">$5.5</span></li>
    <li><span><span class="dish">Add Whipped Mascarpone W/</span> honey</span><span class="price">+$2.5</span></li>
    <li><span><span class="dish">Granola Muesli</span> home made with yoghurt &amp;</span></li>
    <li><span>our own berry compote</span><span class="price">$12.5</span></li>
    <li><span><span class="dish">Spanish Eggs</span> two poached range eggs in a</span></li>
    <li><span>warm spanish tomato salsa topped w/ parmesan</span></li>
    <li><span>cheese with toasted sourdough - $12.5 w/ <span class="dish">Chorizo</span></span><span class="price">$14.5</span></li>
    <li><span><span class="dish">Bacon &amp; Eggs</span> (poached / scrambled or fried)</span></li>
    <li><span>on s/dough toast &amp; side of relish</span><span class="price">$13.5</span></li>
    <li><span><span class="dish">Bacon &amp; Egg Sandwich</span> turkish bread lightly</span></li>
    <li><span>toasted with (2) bacon, fried egg &amp; your choice of</span></li>
    <li><span>house relish / hollandaise / tom or bbq sauce</span><span class="price">$9.0</span></li>
    <li><span><span class="dish">Lifestyle Breakfast</span> wholemeal sourdough topped</span></li>
    <li><span>with wilted baby spinach, asparagus, mushrooms,</span></li>
    <li><span>two poached eggs w/ grilled tomato &amp; fresh avocado</span><span class="price">$17.5</span></li>
    <li><span><span class="dish">Eggs Benedict</span> toasted sourdough w baby spinach,</span></li>
    <li><span>poached eggs &amp; hollandaise sauce</span></li>
    <li><span>$12.5 / w mush$16.5 / w leg ham - $16.5 / w bacon - $16.5 / w</span></li>
    <li><span>salmon</span><span class="price">$18.5</span></li>
    <li><span><span class="dish">The Big Thistle Breakfast</span> toasted sourdough,</span></li>
    <li><span>bacon, eggs (poached, scrambled or fried), chorizo, tomato,</span></li>
    <li><span>mushrooms, baby spinach, hash brown w/ house relish</span><span class="price">$19.5</span></li>
    <li><span><span class="dish">French Toast</span> brioche bread soaked in a creamy</span></li>
    <li><span>cinnamon mix, fried &amp; served with maple syrup,</span></li>
    <li><span>vanilla ice-cream &amp; a side of our berry compote</span><span class="price">$15.5</span></li>
    <li><span><span class="dish">Pancakes</span> two stack of pancakes, topped w maple</span></li>
    <li><span>syrup &amp; ice cream</span><span class="price">$12.5</span></li>
    <li><span class="dish">Add Grilled Banana +$2.0</span></li>
    <li><span><span class="dish">Breakfast Wrap</span> bacon, fried egg, spinach,</span></li>
    <li><span>cheese topped with house made relish</span><span class="price">$13.5</span></li>
    <li><span><span class="dish">Croissants</span> - ham, cheese &amp; tomato</span><span class="price">$8.5</span></li>
    <li><span>or ham, cheese &amp; avocado</span><span class="price">$9.5</span></li>
  </ul>
</main>
</body>
</html>
```